Forensic Psychology and Polygraph Needs Clever Catchy Logo

There's a massive trade show coming up and we are looking to debut a new, clever logo for our business cards. We are a private practice that offers psychological evaluations, therapeutic counseling, and polygraphing. Our website is ketvorin.com (to get a better idea of the color scheme) and instead of the nature/cuddly image that other psychology organizations like to go for, we are interested in cultivating a business, strength, and professional image.
Attached are some popular logos and designs to get those creative juices flowing! I would like to avoid the brain/psi logo as this has been to death so bonus points definitely for originality.
Target Market(s)
governmental agencies, third party mental health providers, individual private pay clients
Industry/Entity Type
Mental Health
Contact Information for Business Card
One one side will be the logo and company name while on the back will be contact information and provider details (name, position, etc)
Look and feel

```html
<!DOCTYPE html>
<html lang="en">
<head>
<meta charset="utf-8">
<title>Ketvorin &amp; Associates – Business Cards</title>
<link rel="stylesheet" href="https://fonts.googleapis.com/css2?family=EB+Garamond:wght@500&family=Montserrat:wght@600&family=Source+Sans+3:wght@400&display=swap">
<style>
  :root {
    --stage: #000000;
    --paper: #ffffff;
    --teal: #1fb0b5;
    --teal-top: #1fa9ac;
    --slate-bottom: #3e4a4b;
    --band: #3f4444;
    --ink: #3a3d3e;
    --ink-soft: #5a5e60;
    --white: #ffffff;
  }
  * { margin: 0; padding: 0; box-sizing: border-box; }
  html, body { width: 1200px; height: 900px; overflow: hidden; background: var(--stage); }
  .canvas { position: relative; width: 1200px; height: 900px; }

  .card {
    position: absolute; top: 271px; width: 457px; height: 281px;
    border-radius: 14px; overflow: hidden;
  }
  .card--front { left: 137px; background: var(--paper); }
  .card--back {
    left: 626px;
    background: linear-gradient(180deg, var(--teal-top) 0%, #23898b 50%, var(--slate-bottom) 100%);
  }

  .holder { position: absolute; left: 28px; top: 25px; }
  .holder__name {
    font-family: "EB Garamond", Georgia, serif; font-weight: 500;
    font-size: 22px; letter-spacing: 0.3px; color: var(--teal); line-height: 1;
  }
  .holder__role {
    font-family: "Source Sans 3", Arial, sans-serif; font-size: 13.5px;
    color: var(--ink-soft); margin-top: 5px; letter-spacing: 0.3px;
  }

  .contact {
    position: absolute; right: 26px; top: 27px;
    font-family: "Source Sans 3", Arial, sans-serif; font-size: 13px; color: var(--ink);
    list-style: none; text-align: right;
  }
  .contact li { display: flex; align-items: center; justify-content: flex-end; gap: 7px; height: 18px; }
  .contact svg { width: 11px; height: 11px; fill: var(--teal); }

  .address {
    position: absolute; right: 25px; top: 147px; text-align: right;
    font-family: "Source Sans 3", Arial, sans-serif; font-size: 13px; line-height: 16.5px;
    color: var(--ink); font-style: normal;
  }

  .brand { position: absolute; text-align: center; }
  .brand__name {
    display: flex; align-items: center; justify-content: center; gap: 8px;
    font-family: "Montserrat", Arial, sans-serif; font-weight: 600; line-height: 1;
  }
  .brand__square { display: inline-block; background: var(--teal); }
  .brand__tag {
    font-family: Arial, Helvetica, sans-serif; letter-spacing: 0.2px; margin-top: 6px;
  }

  .card--front .brand { left: 22px; top: 158px; width: 210px; }
  .card--front .brand__name { font-size: 16.5px; color: var(--ink); }
  .card--front .brand__square { width: 10px; height: 10px; }
  .card--front .brand__tag { font-size: 9.5px; color: #4a4a55; }

  .card--back .brand { left: 0; right: 0; top: 157px; }
  .card--back .brand__name { font-size: 19.5px; color: var(--white); }
  .card--back .brand__square { width: 12px; height: 12px; background: var(--white); }
  .card--back .brand__tag { font-size: 11.5px; color: var(--white); margin-top: 5px; }

  .services {
    position: absolute; left: 0; right: 0; bottom: 0; height: 67px; background: var(--band);
    display: flex; align-items: center; justify-content: center; gap: 9px;
    list-style: none; font-family: "Source Sans 3", Arial, sans-serif; font-size: 15px; color: var(--white);
  }
  .services li { display: flex; align-items: center; gap: 5px; }
  .services li::before { content: ""; width: 4px; height: 4px; background: var(--teal); }
</style>
</head>
<body>
<main class="canvas">
  <section class="card card--front" aria-label="Business card front">
    <div class="holder">
      <p class="holder__name">ELIAS BRANDT</p>
      <p class="holder__role">DIRECTOR</p>
    </div>
    <ul class="contact">
      <li>555.014.2287
        <svg viewBox="0 0 12 12" aria-hidden="true"><path d="M1 4c0-1.5 2.2-2.5 5-2.5S11 2.5 11 4v1H8.5V3.8h-5V5H1z M3 6h6l1.5 4.5h-9z"/></svg>
      </li>
      <li>contact@ketvorin.com
        <svg viewBox="0 0 12 12" aria-hidden="true"><path d="M1 2.5h10v7H1z" /><path d="M1.3 2.8 6 6.5l4.7-3.7" fill="none" stroke="#fff" stroke-width="1"/></svg>
      </li>
    </ul>
    <div class="brand">
      <p class="brand__name"><span class="brand__square"></span>Ketvorin &amp; Associates</p>
      <p class="brand__tag">PSYCHOLOGICAL SERVICES</p>
    </div>
    <address class="address">
      2210 N. Cedar Ridge Rd.<br>
      Suites 101 and<br>
      106 Halden, Arizona 85099
    </address>
    <ul class="services">
      <li>Therapy</li>
      <li>Evaluations</li>
      <li>Consultation</li>
    </ul>
  </section>

  <section class="card card--back" aria-label="Business card back">
    <div class="brand">
      <p class="brand__name"><span class="brand__square"></span>Ketvorin &amp; Associates</p>
      <p class="brand__tag">PSYCHOLOGICAL SERVICES</p>
    </div>
  </section>
</main>
</body>
</html>
```